依頼詳細
高速ジェット船を利用して婚活という事がわかるよう記載
ふたりの約束地めぐり記載
女性は梅原埠頭から乗船、男性は緑川町在住を対象
到着後緑川町内(ふたりの約束地めぐり)を観光
女性が乗船する高速船
往路竹芝7:50 館山9:25 復路 館山16:10竹芝17:25
内容
しおさい広場(お見合い回転ずし・シーグラス等を使った物作り体験)→岬原灯台(車窓)→海鮮の昼食→青葉丘城→北浜桟橋(フリータイム)
※ふたりの約束地 ・北浜桟橋・岬原灯台・青葉丘城
参加費
女性 ¥6,000男性 ¥8,000
画像が必要な場合は以下より使用が可能です。
https://pics.nuvolashare.example/album/Zq83kLmWp2TrXv9BnQe7?key=Hs4Ld8Rk2Mw6Py1Ct5
必ずこちらの画像を使わなければならないというわけではありません。
館山=海・花・海鮮です。
女性受けしそうなチラシをお願いします。

緑川町役所HP
http://www.town.midorikawa.example.jp/index.html
海汽船HP
http://www.seiyokaiun.example.jp/

記載項目
高速ジェット船利用がわかるよう
旅行企画実施:㈱ソラノミチツーリスト(千葉県知事登録旅行業 第2種ー918)
主催:㈱ソラノミチツーリスト 緑川町
後日QR添付
サイズ
A4
ページ数
両面
希望イメージ
シンプル 複雑
単色 カラフル
暗い 明るい
日常 高級
遊び心 厳粛
未来的 伝統的
女性的 男性的
希望する色
納品ファイル
• イラストレーター形式 (.ai)
• PNG形式 (.png)
補足説明
締め切り期間を延長させて頂きます。
西陽海運高速ジェット船を利用する事、ふたりの約束地 鏡ケ浦から富士のみえるまち館山
がわかるようなチラシをよろしくお願い致します。
前回使用した婚活チラシを添付させていただきます。
婚活、その次に観光という形です。南房総観光バスツアー募集みたいな感じではなく
婚活をしたい方対象募集ということがわかるようにお願いいたします。
■ 選んだ理由

海と花のまち館山がうまくデザインされておりまた、今回港活性化事業も目的の一つでもあったのでさり気なく表現されていたことや当日ツアー内容がわかりやすかったため当選させて頂きました。

■ 提案者全員のお礼・コメント

皆様ご提案頂きありがとうございますした。
多くの方が館山の魅力が伝わるデザインをご提案して頂きとても感謝しています。今後も婚活ツアーや婚活パーティー等のチラシ依頼をさせて頂きます。またご縁がありましたら是非ご提案していただければ幸いです。
今回こちらのコンペに参加して頂きありがとうございました。今後ともよろしくお願い致します。

```html
<!DOCTYPE html>
<html lang="ja">
<head>
<meta charset="utf-8">
<title>館山 婚活ツアー</title>
<link href="https://fonts.googleapis.com/css2?family=Noto+Sans+JP:wght@400;700;900&family=Noto+Serif+JP:wght@700;900&display=swap" rel="stylesheet">
<style>
:root{
  --red:#d8283c;
  --pink:#ec6f8e;
  --blue:#1d5ea8;
  --ink:#333;
  --paper:#fff;
  --line:#c9d9ec;
}
*{margin:0;padding:0;box-sizing:border-box}
html,body{width:846px;height:1200px;overflow:hidden;background:var(--paper)}
body{font-family:"Noto Sans JP",sans-serif;color:var(--ink);position:relative}
.photo{position:absolute;border:3px solid var(--paper)}
.sea{background:linear-gradient(180deg,#8fc3e8,#2f7db8 60%,#6a8f4a)}
.flowers{background:linear-gradient(160deg,#f2c24a,#e05b2f 55%,#5a8d3a)}
.sunset{background:linear-gradient(180deg,#f0a04a,#c2452a 60%,#3b2a2a)}
.sculpture{background:linear-gradient(180deg,#bfe0f5,#3a6fc0 70%,#8fb3cf)}
.tulips{background:linear-gradient(170deg,#bde0f0,#e8484f 55%,#4f8a35)}
.fuji{background:linear-gradient(180deg,#f6c36a,#e07b3a 45%,#7a3c3a 70%,#2d3f66)}
.ship{background:linear-gradient(180deg,#d9eefa,#5fa5d8 55%,#1e4f86)}
.wedding{background:linear-gradient(180deg,#f4f1ea,#cfd8e2 60%,#6fa0c8)}
.food{background:linear-gradient(150deg,#f5ece0,#e5735a 50%,#5a3a2a)}
.couple{background:linear-gradient(180deg,#9ccbe8,#d7c6a0 60%,#6f8a4a)}
.castle{background:linear-gradient(180deg,#a8d2f0,#f4f4f0 55%,#3f6b3a)}
.autumn{background:linear-gradient(180deg,#f0c070,#c04a2a 60%,#4d3a2a)}
.bay{background:linear-gradient(180deg,#cde8f7,#3e8cc4 60%,#e8e2cf)}
.bloom{background:linear-gradient(180deg,#8fc5ea,#f1d24a 55%,#d85a8a)}

.tagline{position:absolute;left:40px;top:192px;font:700 20px "Noto Serif JP",serif;color:var(--blue);letter-spacing:.08em;transform:rotate(-4deg);transform-origin:left center}
.title{position:absolute;left:44px;top:226px;font:900 160px/1 "Noto Serif JP",serif;color:var(--red);letter-spacing:.02em}
.badge{position:absolute;left:290px;top:398px;width:130px;height:34px;border-radius:17px;background:var(--pink);color:#fff;font:700 17px/34px "Noto Sans JP",sans-serif;text-align:center}
.lead{position:absolute;left:40px;top:448px;width:410px;font:700 22px/1.55 "Noto Sans JP",sans-serif;color:var(--blue)}
.summary{position:absolute;left:40px;top:532px;width:410px;font-size:12.5px;line-height:1.7}
.fee{position:absolute;left:40px;top:590px;font-size:16px;font-weight:700}
.fee .label{color:var(--blue);margin-right:8px}
.fee .price{color:var(--red);font-size:22px}
.dates{position:absolute;left:40px;top:624px;font-size:15px;font-weight:700;line-height:1.5}
.dates .label{color:var(--blue);margin-right:8px}
.dates .extra{display:block;padding-left:56px}

.info{position:absolute;left:446px;top:748px;width:392px;font-size:12px;line-height:1.65}
.info h3{font-size:13px;color:var(--blue);font-weight:700}
.info .route{margin-bottom:12px}
.info .route b{color:var(--red)}
.steps{list-style:none;margin-top:4px}
.steps li{border:1.5px solid var(--line);border-radius:4px;padding:3px 8px;margin-bottom:6px;background:#f5f9fd;white-space:nowrap}
.steps li.spot{border-color:var(--pink)}
.note{font-size:11.5px;color:var(--pink);margin-top:2px}

.footer{position:absolute;left:0;top:1146px;width:846px;padding:12px 30px 0;font-size:11px;line-height:1.6;color:#444;border-top:1px solid var(--line)}
</style>
</head>
<body>
<div class="photo sea" style="left:0;top:0;width:325px;height:185px" role="img" aria-label="館山の海岸線の写真"></div>
<div class="photo flowers" style="left:325px;top:0;width:160px;height:160px" role="img" aria-label="花畑の写真"></div>
<div class="photo sunset" style="left:485px;top:0;width:155px;height:170px" role="img" aria-label="夕景の海の写真"></div>
<div class="photo sculpture" style="left:640px;top:0;width:206px;height:175px" role="img" aria-label="海辺のモニュメントの写真"></div>

<div class="photo tulips" style="left:465px;top:170px;width:175px;height:115px" role="img" aria-label="チューリップと空の写真"></div>
<div class="photo bay" style="left:640px;top:175px;width:206px;height:110px" role="img" aria-label="鏡ケ浦の写真"></div>
<div class="photo fuji" style="left:465px;top:285px;width:381px;height:320px" role="img" aria-label="桟橋から望む夕日の富士山の写真"></div>

<p class="tagline">西陽海運高速ジェット船で行く</p>
<h1 class="title">館山</h1>
<div class="badge">婚活ツアー</div>

<p class="lead">鏡ケ浦から富士のみえるまち館山の<br>婚活ツアーに参加してみませんか？</p>
<p class="summary">シーグラスを使った物作り体験、海鮮の昼食、ふたりの約束地めぐりなど、館山の海と花を楽しみながら素敵な出会いを見つけましょう。</p>
<p class="fee"><span class="label">参加費</span>女性 <span class="price">¥6,000</span>　男性 <span class="price">¥8,000</span></p>
<p class="dates"><span class="label">日 程</span>2018年00月00日(土)／00月00日(土)<span class="extra">00月00日(土)／00月00日(土)</span></p>

<div class="photo ship" style="left:465px;top:605px;width:175px;height:135px" role="img" aria-label="高速ジェット船の写真"></div>
<div class="photo wedding" style="left:640px;top:605px;width:206px;height:135px" role="img" aria-label="海辺の花嫁の後ろ姿の写真"></div>

<div class="photo food" style="left:0;top:688px;width:228px;height:222px" role="img" aria-label="海鮮料理の写真"></div>
<div class="photo couple" style="left:228px;top:688px;width:200px;height:222px" role="img" aria-label="海辺を歩くふたりの写真"></div>

<section class="info">
  <h3>女性が乗船する高速船</h3>
  <p class="route"><b>【往路】</b>梅原7:50 → 館山9:25　<b>【復路】</b>館山16:10 → 梅原17:25</p>
  <h3>内 容</h3>
  <ul class="steps">
    <li>しおさい広場（お見合い回転ずし・シーグラス等の物作り体験）</li>
    <li class="spot">岬原灯台（車窓） → 海鮮の昼食</li>
    <li class="spot">青葉丘城</li>
    <li class="spot">北浜桟橋（フリータイム）</li>
  </ul>
  <p class="note">※ふたりの約束地 ・北浜桟橋・岬原灯台・青葉丘城</p>
</section>

<div class="photo castle" style="left:0;top:985px;width:200px;height:155px" role="img" aria-label="青葉丘城の写真"></div>
<div class="photo autumn" style="left:200px;top:985px;width:220px;height:155px" role="img" aria-label="紅葉の写真"></div>
<div class="photo sea" style="left:420px;top:985px;width:220px;height:155px" role="img" aria-label="岬と海の写真"></div>
<div class="photo bloom" style="left:640px;top:985px;width:206px;height:155px" role="img" aria-label="海辺の花畑の写真"></div>

<footer class="footer">旅行企画実施：㈱ソラノミチツーリスト（千葉県知事登録旅行業 第2種ー918）　主催：㈱ソラノミチツーリスト 緑川町</footer>
</body>
</html>
```